We need a groovy retro poster for a comedy show called Shimmy Starfield :)

Hi there!
- We need a show poster for a comedy show called "Shimmy Starfield" starring Lydia Brenner.
- We want the show to have a retro groovy 60s/70s vibe with bright colors
- We will need some space to add dates and ticket info later.
- Please use 8.5 x 11 for sizing.

Target Market(s)

Men and women 40 and older, GenX

Industry/Entity Type

Entertainment

Requirements
Must have
• Artist Name: Lydia Brenner
Show Name: Shimmy Starfield
Show Description: A Night of Funky Laughs
Nice to have
• - We would like the headshot photo that is uploaded here to be more of a stylized in a cartoon/illustration way so that it is not just a photo.
- Colorful retro graphics.
- We have provided some samples that we like but are open to other ideas.
- We really like the Disco poster sample that is attached to the brief but would need the lady stylized with hair/face like Lydia
- We also like the style and colors of the Twirl Paradise poster attached to the brief but need the face/hair more like Lydia
- The postcard attached to the brief is just to give an example of branding colors that are currently being used. Not necessary to use them but just to give you an idea.
Should not have
• Please no trite references to stand up comedy such as stage and spotlight. A microphone is ok but only if it fits the illustration.

Thanks!

```html
<!DOCTYPE html>
<html lang="en">
<head>
<meta charset="utf-8">
<title>Shimmy Starfield – Lydia Brenner</title>
<link rel="stylesheet" href="https://fonts.googleapis.com/css2?family=Bungee&family=Chewy&family=Titan+One&family=Poppins:wght@700&display=swap">
<style>
  :root{
    --navy:#14237a;
    --blue:#2f5fd0;
    --sky:#5fb4f0;
    --pale:#cfe9fb;
    --yellow:#ffe11a;
    --magenta:#f03cc8;
    --pink:#ff4fa0;
    --red:#f4364c;
    --orange:#ff9a1f;
    --green:#5fd04a;
    --purple:#8a4ee8;
    --violet:#b06ff0;
    --gold:#e9b820;
    --white:#ffffff;
  }
  html,body{margin:0;padding:0;overflow:hidden;}
  body{width:849px;height:1200px;}
  .poster{
    position:relative;width:849px;height:1200px;overflow:hidden;
    background:linear-gradient(180deg,var(--navy) 0%,#1f3aa8 35%,var(--blue) 60%,var(--sky) 85%,var(--pale) 100%);
    font-family:"Poppins",sans-serif;
  }
  .shapes{position:absolute;inset:0;}
  .tagline{
    position:absolute;top:34px;left:0;width:100%;text-align:center;margin:0;
    font-family:"Chewy","Titan One",sans-serif;font-size:50px;line-height:1.1;color:var(--yellow);
    letter-spacing:1px;
  }
  .show-title{position:absolute;top:110px;left:0;width:100%;text-align:center;margin:0;font-weight:400;}
  .show-title .line1{
    display:block;font-family:"Titan One",sans-serif;font-size:124px;line-height:1;letter-spacing:2px;
  }
  .line1 .c1{color:var(--red);} .line1 .c2{color:var(--orange);} .line1 .c3{color:var(--yellow);}
  .line1 .c4{color:var(--green);} .line1 .c5{color:var(--purple);} .line1 .c6{color:var(--violet);}
  .show-title .line2{
    display:block;margin-top:36px;font-family:"Bungee",sans-serif;font-size:76px;line-height:1;color:var(--magenta);
  }
  .record{position:absolute;left:212px;top:880px;width:490px;height:230px;}
  .dancer{
    position:absolute;left:425px;top:372px;width:340px;height:690px;border-radius:150px 150px 60px 60px;
    background:linear-gradient(180deg,#f3e6b8 0%,#e9c98a 18%,#2a2a3a 34%,#3a3a3a 48%,#5f9a3a 62%,#3e7a2a 100%);
    opacity:.85;
  }
  .star-name{
    position:absolute;left:56px;top:720px;margin:0;font-weight:400;
    font-family:"Bungee",sans-serif;color:var(--pink);line-height:.95;
  }
  .star-name .first{display:block;font-size:64px;margin-left:34px;}
  .star-name .last{display:block;font-size:70px;}
  .site{
    position:absolute;left:110px;top:880px;padding:6px 18px;border-radius:20px;
    background:var(--white);color:var(--red);font-size:20px;letter-spacing:1px;
  }
</style>
</head>
<body>
<main class="poster">
  <svg class="shapes" width="849" height="1200" viewBox="0 0 849 1200" aria-hidden="true">
    <polygon points="40,260 120,215 95,310" fill="var(--magenta)"/>
    <polygon points="700,140 800,110 780,205" fill="var(--pink)" opacity=".9"/>
    <rect x="755" y="30" width="60" height="60" fill="var(--violet)" transform="rotate(20 785 60)"/>
    <rect x="30" y="20" width="70" height="16" fill="var(--pink)" transform="rotate(-25 65 28)"/>
    <rect x="560" y="8" width="18" height="48" fill="var(--magenta)"/>
    <rect x="190" y="420" width="10" height="90" fill="var(--pink)" transform="rotate(-35 195 465)"/>
    <rect x="760" y="420" width="14" height="110" fill="var(--pink)" transform="rotate(30 767 475)"/>
    <circle cx="180" cy="445" r="30" fill="var(--magenta)"/>
    <circle cx="320" cy="570" r="55" fill="none" stroke="var(--yellow)" stroke-width="6"/>
    <circle cx="800" cy="310" r="26" fill="none" stroke="var(--yellow)" stroke-width="4"/>
    <circle cx="210" cy="640" r="85" fill="var(--pale)" opacity=".35"/>
    <rect x="40" y="560" width="120" height="120" fill="var(--pale)" opacity=".35" transform="rotate(12 100 620)"/>
    <rect x="720" y="880" width="70" height="70" fill="var(--pale)" opacity=".6"/>
    <rect x="780" y="620" width="22" height="100" fill="var(--pink)" transform="rotate(-20 791 670)"/>
    <circle cx="120" cy="1130" r="120" fill="var(--pale)" opacity=".7"/>
    <circle cx="720" cy="1160" r="90" fill="var(--white)" opacity=".35"/>
    <path d="M450 1130 l8 18 l18 8 l-18 8 l-8 18 l-8-18 l-18-8 l18-8z" fill="var(--yellow)"/>
    <path d="M160 1020 l6 14 l14 6 l-14 6 l-6 14 l-6-14 l-14-6 l14-6z" fill="var(--yellow)"/>
    <path d="M800 1000 l5 12 l12 5 l-12 5 l-5 12 l-5-12 l-12-5 l12-5z" fill="var(--yellow)"/>
  </svg>

  <p class="tagline">A Night of Funky Laughs</p>

  <h1 class="show-title">
    <span class="line1"><span class="c1">S</span><span class="c2">H</span><span class="c3">I</span><span class="c4">M</span><span class="c5">M</span><span class="c6">Y</span></span>
    <span class="line2">STARFIELD</span>
  </h1>

  <svg class="record" viewBox="0 0 490 230" role="img" aria-label="Illustrated gold vinyl record the performer dances on">
    <ellipse cx="245" cy="115" rx="243" ry="110" fill="var(--gold)"/>
  </svg>

  <div class="dancer" role="img" aria-label="Cartoon illustration of Lydia Brenner dancing in a black top and green patterned flared trousers"></div>

  <h2 class="star-name"><span class="first">LYDIA</span><span class="last">BRENNER</span></h2>
  <div class="site">lydiabrenner.show</div>
</main>
</body>
</html>
```